Amber Vital 720

This is a 9 week program we conduct in our gym/recovery facility with the aim of educating members on the ins and outs of training, sauna use, cold plunge, sleep and lifestyle factors that they need to consider to increase health span into their older age. It is geared towards the Gen X age group.

```html
<!DOCTYPE html>
<html lang="en">
<head>
<meta charset="utf-8">
<title>Amber Vital 720</title>
<link href="https://fonts.googleapis.com/css2?family=Lora:wght@700&family=Roboto:wght@400;500;700&display=swap" rel="stylesheet">
<style>
:root{
  --navy:#1f3677;
  --ink:#1b1b1d;
  --grey:#b3b3b3;
  --text:#2a2a2a;
  --pale:#f2f3f7;
  --white:#ffffff;
  --line:#d9dbe3;
}
*{box-sizing:border-box;margin:0;padding:0}
html,body{width:1200px;height:3645px;overflow:hidden}
body{position:relative;font-family:'Roboto',sans-serif;color:var(--text);background:var(--white)}
.abs{position:absolute}
.serif{font-family:'Lora',serif;font-weight:700}
.btn{position:absolute;display:flex;align-items:center;justify-content:center;border-radius:30px;background:var(--navy);color:var(--white);font-weight:700;text-transform:uppercase}
.topline{left:0;top:0;width:1200px;height:5px;background:var(--navy)}
.logo{color:var(--navy);font-size:28px;line-height:36px}
.nav a{position:absolute;top:60px;font-size:15px;color:#333;text-decoration:none}
.nav a.active{color:var(--navy);text-decoration:underline}
.social{position:absolute;width:36px;height:36px;border-radius:50%;border:1.5px solid var(--navy)}
.social.filled{background:var(--navy)}
.hero{left:0;top:138px;width:1200px;height:650px;background:linear-gradient(100deg,#c8a77a 0%,#b08a57 30%,#d8c2a0 55%,#e9dcc6 80%,#f1e6d4 100%)}
.hero h1{position:absolute;left:111px;top:160px;font-size:44px;color:var(--ink)}
.hero p{position:absolute;left:111px;top:222px;width:480px;font-size:20px;line-height:30px;color:var(--ink)}
.dot{position:absolute;top:466px;width:15px;height:15px;border-radius:50%;border:2px solid var(--white)}
.dot.on{background:var(--white)}
.heading{font-size:44px;color:var(--ink)}
.heading span{color:var(--grey)}
.story p{font-size:14.5px;line-height:25.7px;text-align:justify;color:var(--text);margin-bottom:10px}
.facilities{left:0;top:1360px;width:1200px;height:717px;background:var(--pale)}
.fac{position:absolute;top:0;width:248px;text-align:center}
.fac .ring{margin:228px auto 0;width:208px;height:208px;border-radius:50%;border:2px solid #c9cbd3;padding:12px}
.fac .ring.sel{border-color:var(--navy)}
.fac .photo{width:100%;height:100%;border-radius:50%}
.fac h3{margin-top:26px;font-size:17px;font-weight:500;color:var(--ink)}
.fac .pip{width:9px;height:9px;border-radius:50%;background:#cfd1d8;margin:11px auto 10px}
.fac p{font-size:13.5px;line-height:24px;color:var(--text)}
.fac .more{margin:16px auto 0;width:108px;height:38px;border-radius:20px;background:var(--white);box-shadow:0 4px 10px rgba(0,0,0,.12);font-size:11.5px;font-weight:700;color:var(--navy);display:flex;align-items:center;justify-content:center}
.fac .more.sel{background:var(--navy);color:var(--white)}
.band{left:0;top:2077px;width:1200px;height:415px;background:var(--navy)}
.card{position:absolute;top:2261px;width:307px;height:445px;background:var(--white);border-radius:22px;box-shadow:0 8px 22px rgba(31,54,119,.18);text-align:center}
.card .photo{margin:8px;height:218px;border-radius:18px}
.card .date{margin-top:17px;font-size:13.5px;color:var(--text)}
.card h3{margin-top:8px;font-size:17px;font-weight:500;color:var(--ink)}
.card p{margin:8px 16px 0;font-size:14.5px;line-height:24px;color:#444}
.card .more{margin:14px auto 0;width:108px;height:36px;border-radius:20px;background:var(--navy);color:var(--white);font-size:11.5px;font-weight:700;display:flex;align-items:center;justify-content:center}
.arrow{position:absolute;top:2362px}
.field{position:absolute;background:var(--white);box-shadow:0 3px 10px rgba(0,0,0,.07);font-size:14px;color:#555;padding:16px 17px}
.footer{left:0;top:3310px;width:1200px;height:335px;background:var(--ink)}
.footer h4{position:absolute;top:36px;font-size:17px;font-weight:500;color:var(--white)}
.footer .item{position:absolute;font-size:14px;color:var(--white);line-height:20px}
.bullet{position:absolute;width:11px;height:11px;border-radius:50%;border:3px solid var(--navy)}
.ficon{position:absolute;width:36px;height:36px;border-radius:50%;background:var(--white);display:flex;align-items:center;justify-content:center}
</style>
</head>
<body>
<div class="abs topline"></div>

<header>
  <div class="abs logo serif" style="left:110px;top:33px">AMBER<br>VITAL 720</div>
  <nav class="nav">
    <a class="active" style="left:350px" href="#">Home</a>
    <a style="left:418px" href="#">About</a>
    <a style="left:486px" href="#">Programs</a>
    <a style="left:581px" href="#">Contact Us</a>
  </nav>
  <div class="abs" style="left:689px;top:38px;width:1px;height:62px;background:var(--line)"></div>
  <span class="social filled" style="left:719px;top:53px" role="img" aria-label="Social profile"></span>
  <span class="social" style="left:760px;top:53px" role="img" aria-label="Social profile"></span>
  <span class="social" style="left:801px;top:53px" role="img" aria-label="Social profile"></span>
  <div class="abs" style="left:860px;top:48px;width:44px;height:44px;border-radius:50%;background:var(--white);box-shadow:0 3px 10px rgba(0,0,0,.15);display:flex;align-items:center;justify-content:center">
    <svg width="18" height="18" viewBox="0 0 24 24"><path fill="#1f3677" d="M6.6 10.8c1.4 2.8 3.8 5.1 6.6 6.6l2.2-2.2c.3-.3.7-.4 1-.2 1.1.4 2.3.6 3.6.6.6 0 1 .4 1 1V20c0 .6-.4 1-1 1C10.6 21 3 13.4 3 4c0-.6.4-1 1-1h3.5c.6 0 1 .4 1 1 0 1.2.2 2.4.6 3.6.1.3 0 .7-.2 1z"/></svg>
  </div>
  <div class="abs" style="left:918px;top:48px;font-size:12px;color:#444">CALL US:</div>
  <div class="abs" style="left:918px;top:67px;font-size:20px;font-weight:500;color:var(--ink)">+1 (555) 010 0720</div>
</header>

<section class="abs hero" role="img" aria-label="Photo of a smiling couple jogging outdoors at sunset">
  <h1 class="serif">AMBER VITAL 720</h1>
  <p>Lorem ipsum dolor sit amet, consectetur adipiscing elit, sed do eiusmod temea.</p>
  <a class="btn" style="left:111px;top:310px;width:146px;height:50px;font-size:14.5px">Get Started</a>
  <span class="dot" style="left:111px"></span>
  <span class="dot on" style="left:137px"></span>
  <span class="dot" style="left:162px"></span>
  <span class="dot" style="left:188px"></span>
</section>
<svg class="abs" style="left:0;top:600px" width="1200" height="190" viewBox="0 0 1200 190">
  <path fill="#1f3677" d="M0 128 C250 4 450 14 700 96 C900 158 1050 108 1200 26 L1200 44 C1050 124 900 172 700 112 C450 32 250 22 0 142Z"/>
  <path fill="#ffffff" d="M0 142 C250 22 450 32 700 112 C900 172 1050 124 1200 44 L1200 190 L0 190Z"/>
  <path fill="#d0d0d2" d="M600 120 C820 210 1000 180 1200 46 L1200 56 C1000 196 800 218 600 120Z"/>
</svg>

<section class="story">
  <div class="abs" style="left:111px;top:815px;width:430px;height:430px;border-radius:50%;background:var(--navy)"></div>
  <div class="abs" style="left:150px;top:840px;width:384px;height:384px;border-radius:50%;background:linear-gradient(135deg,#d9d39a,#8fa86a 45%,#c7cfd3 80%)" role="img" aria-label="Photo of older adults stretching together in a park"></div>
  <h2 class="abs heading serif" style="left:600px;top:838px">OUR <span>STORY</span></h2>
  <div class="abs" style="left:600px;top:910px;width:489px">
    <p>Lorem ipsum dolor sit amet, consectetur adipiscing elit, sed do eiusmod tempor incididunt ut labore et dolore magna aliqua. Ut enim ad minim veniam, quis nostrud exercitation ullamco laboris nisi ut aliquip ex ea commodo consequat. Duis aute irure dolor in reprehenderit in voluptate velit esse cillum dolore eu fugiatea.</p>
    <p>Lorem ipsum dolor sit amet, consectetur adipiscing elit, sed do eiusmod tempor incididunt ut labore et dolore magna aliqua. Ut enim ad minim veniam, quis nostrudea.</p>
  </div>
  <a class="btn" style="left:601px;top:1159px;width:146px;height:50px;font-size:14.5px">Learn More</a>
</section>

<section class="abs facilities">
  <h2 class="abs heading serif" style="left:0;width:1200px;text-align:center;top:72px">OUR <span>FACILITIES</span></h2>
  <p class="abs" style="left:125px;width:950px;top:144px;text-align:center;font-size:14.5px;line-height:26px">Lorem ipsum dolor sit amet, consectetur adipiscing elit, sed do eiusmod tempor incididunt ut labore et dolore magna aliqua. Ut enim ad minim veniam, quis nostrud exercitation ullamco laboris nisi ut aliquipea.</p>
  <div class="fac" style="left:102px">
    <div class="ring"><div class="photo" role="img" aria-label="Photo of an older couple walking in a park" style="background:linear-gradient(160deg,#6f8a45,#c9c7b8)"></div></div>
    <h3>OUTS OF TRAINING</h3><div class="pip"></div>
    <p>Lorem ipsum dolor sit amet, consect adipiscing elit, sed do eiusmod tempor incididuntea.</p>
    <div class="more">READ MORE</div>
  </div>
  <div class="fac" style="left:350px">
    <div class="ring"><div class="photo" role="img" aria-label="Photo of a woman relaxing in a wooden sauna" style="background:linear-gradient(160deg,#a8552a,#d99a6a)"></div></div>
    <h3>SAUNA USE</h3><div class="pip"></div>
    <p>Lorem ipsum dolor sit amet, consect adipiscing elit, sed do eiusmod tempor incididuntea.</p>
    <div class="more">READ MORE</div>
  </div>
  <div class="fac" style="left:599px">
    <div class="ring sel"><div class="photo" role="img" aria-label="Photo of an older man in an ice bath" style="background:linear-gradient(160deg,#5f7f98,#c9dce8)"></div></div>
    <h3>COLD PLUNGE</h3><div class="pip"></div>
    <p>Lorem ipsum dolor sit amet, consect adipiscing elit, sed do eiusmod tempor incididuntea.</p>
    <div class="more sel">READ MORE</div>
  </div>
  <div class="fac" style="left:848px">
    <div class="ring"><div class="photo" role="img" aria-label="Photo of an older couple resting in bed" style="background:linear-gradient(160deg,#b9b6b0,#e6e2de)"></div></div>
    <h3>SLEEP AND LIFESTYLE</h3><div class="pip"></div>
    <p>Lorem ipsum dolor sit amet, consect adipiscing elit, sed do eiusmod tempor incididuntea.</p>
    <div class="more">READ MORE</div>
  </div>
</section>

<section class="abs band">
  <h2 class="abs heading serif" style="left:0;width:1200px;text-align:center;top:80px;color:var(--white)">WEEK PROGRAMS</h2>
</section>
<svg class="arrow" style="left:38px" width="40" height="24" viewBox="0 0 40 24"><path d="M38 12H3M13 2L3 12l10 10" stroke="#fff" stroke-width="2" fill="none"/></svg>
<svg class="arrow" style="left:1122px" width="40" height="24" viewBox="0 0 40 24"><path d="M2 12h35M27 2l10 10-10 10" stroke="#fff" stroke-width="2" fill="none"/></svg>

<article class="card" style="left:111px">
  <div class="photo" role="img" aria-label="Photo of two older men in cold water wearing knit hats" style="background:linear-gradient(160deg,#7b9aa6,#c4d4d8)"></div>
  <div class="date">&#128197; 28 Sep 2024</div>
  <h3>LOREM IPSUM DOLOR</h3>
  <p>Lorem ipsum dolor sit amet, consectetu adipiscing elit, sed do eiusmod tempor incididunt ut laborea.</p>
  <div class="more">READ MORE</div>
</article>
<article class="card" style="left:446px">
  <div class="photo" role="img" aria-label="Photo of an older couple walking a dog outdoors" style="background:linear-gradient(160deg,#6e8a4a,#c6c9bd)"></div>
  <div class="date">&#128197; 28 Sep 2024</div>
  <h3>LOREM IPSUM DOLOR</h3>
  <p>Lorem ipsum dolor sit amet, consectetu adipiscing elit, sed do eiusmod tempor incididunt ut laborea.</p>
  <div class="more">READ MORE</div>
</article>
<article class="card" style="left:781px">
  <div class="photo" role="img" aria-label="Photo of an older woman pouring water in a sauna" style="background:linear-gradient(160deg,#9a5530,#e3c7ae)"></div>
  <div class="date">&#128197; 28 Sep 2024</div>
  <h3>LOREM IPSUM DOLOR</h3>
  <p>Lorem ipsum dolor sit amet, consectetu adipiscing elit, sed do eiusmod tempor incididunt ut laborea.</p>
  <div class="more">READ MORE</div>
</article>

<section class="contact">
  <h2 class="abs heading serif" style="left:0;width:1200px;text-align:center;top:2808px">GET IN <span>TOUCH</span></h2>
  <div class="field" style="left:166px;top:2906px;width:282px;height:48px">Full Name</div>
  <div class="field" style="left:458px;top:2906px;width:283px;height:48px">Phone Number</div>
  <div class="field" style="left:751px;top:2906px;width:283px;height:48px">Email Address</div>
  <div class="field" style="left:166px;top:2968px;width:868px;height:94px">Message</div>
  <a class="btn" style="left:519px;top:3076px;width:162px;height:48px;font-size:15px">Send Message</a>
</section>

<svg class="abs" style="left:0;top:3150px" width="1200" height="170" viewBox="0 0 1200 170">
  <path fill="#d0d0d2" d="M0 150 C150 40 350 20 590 112 C350 46 150 66 0 162Z"/>
  <path fill="#1f3677" d="M0 148 C300 50 500 160 750 150 C950 140 1100 70 1200 28 L1200 42 C1100 84 950 154 750 164 C500 174 300 64 0 162Z"/>
  <path fill="#1b1b1d" d="M0 162 C300 64 500 174 750 164 C950 154 1100 84 1200 42 L1200 170 L0 170Z"/>
</svg>

<footer class="abs footer">
  <div class="abs serif" style="left:111px;top:106px;font-size:30px;line-height:38px;color:var(--white)">AMBER<br>VITAL 720</div>

  <h4 style="left:345px">OTHER LINKS</h4>
  <span class="bullet" style="left:347px;top:92px"></span><span class="item" style="left:380px;top:86px">Home</span>
  <span class="bullet" style="left:347px;top:126px"></span><span class="item" style="left:380px;top:120px">About</span>
  <span class="bullet" style="left:347px;top:160px"></span><span class="item" style="left:380px;top:154px">Programs</span>
  <span class="bullet" style="left:347px;top:195px"></span><span class="item" style="left:380px;top:189px">Blog</span>
  <span class="bullet" style="left:347px;top:229px"></span><span class="item" style="left:380px;top:223px">Contact Us</span>

  <h4 style="left:515px">CONTACT US</h4>
  <div class="ficon" style="left:515px;top:82px"><svg width="14" height="16" viewBox="0 0 24 24"><path fill="#1f3677" d="M12 2a7 7 0 0 0-7 7c0 5 7 13 7 13s7-8 7-13a7 7 0 0 0-7-7zm0 9.5A2.5 2.5 0 1 1 12 6.5a2.5 2.5 0 0 1 0 5z"/></svg></div>
  <span class="item" style="left:569px;top:86px">720 Amber Way,<br>Springfield</span>
  <div class="ficon" style="left:515px;top:132px"><svg width="14" height="14" viewBox="0 0 24 24"><path fill="#1f3677" d="M3 5h18v14H3z"/><path d="M3 6l9 7 9-7" stroke="#fff" stroke-width="2" fill="none"/></svg></div>
  <span class="item" style="left:569px;top:140px">info@ambervital720.com</span>
  <div class="ficon" style="left:515px;top:183px"><svg width="14" height="14" viewBox="0 0 24 24"><path fill="#1f3677" d="M6.6 10.8c1.4 2.8 3.8 5.1 6.6 6.6l2.2-2.2c.3-.3.7-.4 1-.2 1.1.4 2.3.6 3.6.6.6 0 1 .4 1 1V20c0 .6-.4 1-1 1C10.6 21 3 13.4 3 4c0-.6.4-1 1-1h3.5c.6 0 1 .4 1 1 0 1.2.2 2.4.6 3.6.1.3 0 .7-.2 1z"/></svg></div>
  <span class="item" style="left:569px;top:191px">+1 (555) 010 0720</span>

  <h4 style="left:800px">NEWSLETTER</h4>
  <span class="item" style="left:800px;top:86px">Email</span>
  <div class="abs" style="left:800px;top:112px;width:286px;height:2px;background:var(--white)"></div>
  <a class="btn" style="left:802px;top:128px;width:130px;height:48px;font-size:15px;text-transform:none">SUBSCRIBE</a>

  <div class="abs" style="left:111px;top:267px;width:978px;height:1px;background:#3a3a3e"></div>
  <div class="abs" style="left:0;width:1200px;top:290px;text-align:center;font-size:13px;color:var(--white)">© 2024 <b style="font-weight:500">AMBER VITAL 720</b> &nbsp;|&nbsp; Privacy Policy • Terms &amp; Conditions</div>
  <span class="social filled" style="left:969px;top:280px;border-color:#fff" role="img" aria-label="Social profile"></span>
  <span class="social" style="left:1011px;top:280px;border-color:#fff" role="img" aria-label="Social profile"></span>
  <span class="social" style="left:1052px;top:280px;border-color:#fff" role="img" aria-label="Social profile"></span>
</footer>
</body>
</html>
```